Website for Party

Design a new website for PlumtreeGatherings.net
We have attached the new logos and please look at the website, and our facebook page: facebook.com/plumtreegatherings for inspiration
Updates

Hi Guys, please be original with all designs and images otherwise the design will be eliminated Thank you

some of your designs have too much happening in them, others make it clear that the designer has not yet read the brief fully

Please everyone be original!

```html
<!DOCTYPE html>
<html lang="en">
<head>
<meta charset="utf-8">
<title>Plumtree Gatherings</title>
<link href="https://fonts.googleapis.com/css2?family=Arimo:ital,wght@0,400;0,700;1,400&display=swap" rel="stylesheet">
<style>
:root{
  --ink:#0b0b0b;
  --panel:#141414;
  --band:#1b1b1b;
  --band-dark:#111;
  --orange:#e05a12;
  --orange-card:#c9520f;
  --text:#d8d8d8;
  --muted:#8a8a8a;
  --white:#fff;
}
*{box-sizing:border-box;margin:0;padding:0}
html,body{width:1032px;height:1200px;overflow:hidden}
body{position:relative;font-family:"Arimo",Arial,sans-serif;color:var(--text);background:#120806}
.backdrop{position:absolute;inset:0;
  background:
   radial-gradient(circle at 88% 85%,rgba(230,110,40,.55),transparent 28%),
   radial-gradient(circle at 8% 70%,rgba(200,90,30,.45),transparent 30%),
   radial-gradient(circle at 92% 15%,rgba(160,70,40,.5),transparent 30%),
   radial-gradient(circle at 6% 15%,rgba(90,110,60,.45),transparent 28%),
   linear-gradient(180deg,#2a1410,#3a1a0e 60%,#2a0f08)}
.site{position:absolute;left:147px;top:13px;width:739px;height:1171px;background:var(--ink);border-radius:8px 8px 0 0;overflow:hidden}
.abs{position:absolute}
.brand{left:16px;top:28px;font-size:30px;font-weight:700;color:var(--white);letter-spacing:1px}
.brand-sub{left:16px;top:70px;font-size:12px;font-weight:700;color:var(--white);letter-spacing:3px}
.social{right:14px;top:24px;display:flex;gap:9px}
.social span{width:21px;height:21px;background:#cfcfcf;border-radius:2px}
.nav{left:353px;top:64px;width:373px;height:35px;border-top:1px solid #555;border-bottom:1px solid #555;display:flex;align-items:center;justify-content:space-between;padding:0 5px;font-size:13px;color:#9a9a9a}
.nav .active{color:var(--orange)}
.hero{left:0;top:119px;width:739px;height:296px;background:linear-gradient(180deg,#f0c060 0%,#b06a20 35%,#3a2010 75%,#120a06)}
.events{left:0;top:415px;width:739px;height:303px;background:var(--band-dark)}
h2{position:absolute;font-size:18px;font-weight:700;color:var(--white);letter-spacing:.3px}
.arrows{right:14px;top:22px;display:flex;gap:4px}
.card{position:absolute;top:48px;width:171px;height:237px}
.card .pic{height:148px}
.card .body{height:89px;background:var(--orange-card);padding:8px 8px}
.card h3{font-size:14px;color:var(--white);font-weight:700;margin-bottom:6px}
.card p{font-size:10.5px;line-height:16px;color:#f7dccb}
.testimonials{left:0;top:718px;width:739px;height:138px;background:var(--band)}
.portrait{left:13px;top:49px;width:91px;height:65px;border:2px solid #666;background:linear-gradient(160deg,#8a6a55,#3a2a22)}
.quote{left:134px;top:52px;width:594px;font-size:10.5px;line-height:16px;font-style:italic;color:var(--muted)}
.qmark{color:var(--orange);font-size:20px;font-style:normal;font-family:Georgia,serif}
.author{left:134px;top:108px;font-size:10.5px;font-style:italic;color:var(--orange)}
.more{color:var(--orange)}
.lower{left:0;top:856px;width:739px;height:259px;background:var(--panel)}
.dj-photo{left:13px;top:50px;width:237px;height:121px;border:3px solid #eee;background:linear-gradient(135deg,#3b2a6a,#1a1030 55%,#6a4a9a)}
.small{font-size:10.5px;line-height:16px;color:#cfcfcf}
.news-item{position:absolute;left:332px;width:195px;border-bottom:1px solid #333;padding-bottom:6px}
.news-item .date{font-size:12px;color:var(--white);margin-bottom:4px}
.news-item .date a{color:var(--orange);text-decoration:none}
.news-item .small{color:#999}
.dj-list{left:612px;top:54px;list-style:none}
.dj-list li{font-size:10.5px;color:var(--orange);height:22px;position:relative;padding-left:18px}
.dj-list li::before{content:"";position:absolute;left:0;top:4px;width:6px;height:6px;background:#eee}
.footer{left:0;top:1115px;width:739px;height:56px;background:var(--band-dark);text-align:center;font-size:10.5px;color:#555;padding-top:12px;line-height:17px}
</style>
</head>
<body>
<div class="backdrop" role="img" aria-label="Blurred orange party lights with guests on either side"></div>
<div class="site">
  <div class="abs brand">Plumtree</div>
  <div class="abs brand-sub">GATHERINGS</div>
  <div class="abs social" aria-label="Social links"><span></span><span></span><span></span><span></span><span></span></div>
  <nav class="abs nav"><span class="active">Welcome</span><span>About</span><span>FAQ</span><span>Order Tickets</span><span>Contact</span></nav>

  <div class="abs hero" role="img" aria-label="Crowd with raised hands at a concert under warm stage lights"></div>

  <section class="abs events">
    <h2 style="left:13px;top:15px">UPCOMING EVENTS</h2>
    <div class="abs arrows">
      <svg width="18" height="20" viewBox="0 0 18 20"><rect width="18" height="20" fill="#222"/><path d="M12 4 6 10l6 6" stroke="#ccc" stroke-width="3" fill="none"/></svg>
      <svg width="18" height="20" viewBox="0 0 18 20"><rect width="18" height="20" fill="#222"/><path d="M6 4l6 6-6 6" stroke="#ccc" stroke-width="3" fill="none"/></svg>
    </div>
    <article class="card" style="left:13px"><div class="pic" role="img" aria-label="Two friends with cocktails" style="background:linear-gradient(135deg,#e0a070,#7a3a20)"></div><div class="body"><h3>3+ Hour Cruise</h3><p>Lorem ipsum dolor sit amet, consectetuer adipiscing elit, sed diam nonummy nibh euismod...</p></div></article>
    <article class="card" style="left:193px"><div class="pic" role="img" aria-label="White bar counter with red stools" style="background:linear-gradient(180deg,#8a8a8a,#eaeaea 60%,#bbb)"></div><div class="body"><h3>Open Premium Bar</h3><p>Lorem ipsum dolor sit amet, consectetuer adipiscing elit, sed diam nonummy nibh euismod...</p></div></article>
    <article class="card" style="left:373px"><div class="pic" role="img" aria-label="Plated prawn appetizers" style="background:linear-gradient(180deg,#f2f2f2,#e8a060 65%,#f0f0f0)"></div><div class="body"><h3>Hors d'oeuvres</h3><p>Lorem ipsum dolor sit amet, consectetuer adipiscing elit, sed diam nonummy nibh euismod...</p></div></article>
    <article class="card" style="left:553px"><div class="pic" role="img" aria-label="Singer performing on a blue-lit stage" style="background:linear-gradient(135deg,#1a1a5a,#3030a0 55%,#8a2040)"></div><div class="body"><h3>Opening Performance</h3><p>Lorem ipsum dolor sit amet, consectetuer adipiscing elit, sed diam nonummy nibh euismod...</p></div></article>
  </section>

  <section class="abs testimonials">
    <h2 style="left:13px;top:14px">TESTIMONIALS</h2>
    <div class="abs portrait" role="img" aria-label="Portrait of a guest"></div>
    <p class="abs quote"><span class="qmark">“</span> Lorem ipsum dolor sit amet, consectetuer adipiscing elit, sed diam nonummy nibh euismod tincidunt ut laoreet dolore magna aliquam erat volutpat. Ut wisi enim ad minim veniam, quis nostrud exerci tation ullamcorper suscipit lobortis nisl ut aliquip ex ea commodo consequat. Duis autem vel eum iriure dolor in hendrerit in vulputate velit esse molestie consequat, <span class="qmark">”</span></p>
    <div class="abs author">( Nora Whitfield )</div>
    <div class="abs small more" style="right:14px;top:108px">[Read More]</div>
  </section>

  <section class="abs lower">
    <h2 style="left:13px;top:18px">WELCOME</h2>
    <div class="abs dj-photo" role="img" aria-label="DJ mixing at turntables under purple lights"></div>
    <p class="abs small" style="left:13px;top:186px;width:235px">Lorem ipsum dolor sit amet, consectetuer adipiscing elit, sed diam nonummy nibh euismod tincidunt ut laoreet dolore magna...<span class="more">[Read More]</span></p>

    <h2 style="left:332px;top:18px">FRESH NEWS</h2>
    <div class="news-item" style="top:56px"><div class="date">14.Sept <a>Meytasa Luytsas</a></div><p class="small">Lorem ipsum dolor sit amet, consectetuer adipiscing elit, sed diam...<span class="more">[Read More]</span></p></div>
    <div class="news-item" style="top:121px"><div class="date">14.Sept <a>Meytasa Luytsas</a></div><p class="small">Lorem ipsum dolor sit amet, consectetuer adipiscing elit, sed diam...<span class="more">[Read More]</span></p></div>
    <div class="news-item" style="top:186px;border:0"><div class="date">14.Sept <a>Meytasa Luytsas</a></div><p class="small">Lorem ipsum dolor sit amet, consectetuer adipiscing elit, sed diam...<span class="more">[Read More]</span></p></div>

    <h2 style="left:610px;top:18px">DJ SETS</h2>
    <ul class="abs dj-list">
      <li>Asefy kscabo</li><li>Nerafaes</li><li>Kertyu ersvitae</li><li>Ertyasnemo lasecas</li><li>Asptaiades goert</li><li>Ayse volematur</li><li>Aut oditaut</li><li>Onsequuntur magni</li><li>Dolores eos</li>
    </ul>
  </section>

  <footer class="abs footer">
    <div>Welcome &nbsp;|&nbsp; About &nbsp;|&nbsp; FAQ &nbsp;|&nbsp; Order Tickets &nbsp;|&nbsp; Contact</div>
    <div>Copyright © 2014 PlumtreeGatherings.net. All Rights Reserved.</div>
  </footer>
</div>
</body>
</html>
```